Velvetorchid Hair & Beauty Business Card

Velvetorchid Hair & Beauty is a boutique salon located in the picturesque Lake Taupo NZ. The salon is very luxurious, opulent gold gilded mirrors, chandelier lit, contemporary french decor, sets the mood to create beautiful hair, makeup and all beauty services. Just had a new logo design and now after a new business card.
Logo
14 Kerewhenua Street
Taupo
Phone (07) 384 6139
www.velvetorchid.co.nz
email hair@velvetorchid.co.nz
Lorinda Feltham
Also need a space to put in Stylist name, date, appointment time. thanks;)
Another idea is we could incorporate the wallpaper in the back ground either on the back or front or use an ornate glided frame (around the edge of the card) like on my website where my brides photos flash.
Decided against the wall paper but at least you can see our colour theme for the salon.
Updates

Please check out my updated brief . Thanks :)

Target Market(s)

25-60 years plus, mainly mid age females , wanting the best possible service , high standard of workmanship and money not a problem.

Industry/Entity Type

Boutique

Requirements
Must have
• Gold and silver

```html
<!DOCTYPE html>
<html lang="en">
<head>
<meta charset="utf-8">
<title>Velvetorchid Hair &amp; Beauty – Business Card</title>
<link rel="stylesheet" href="https://fonts.googleapis.com/css2?family=Questrial&family=Roboto+Condensed:wght@400&family=Roboto:wght@500&display=swap">
<style>
  :root {
    --backdrop: #ece9e4;
    --card: #ffffff;
    --gold: #8a6d2c;
    --gold-deep: #6f5520;
    --gold-light: #d8c27a;
    --frame-dark: #4a4320;
    --ornament: #c9ae62;
    --silver: #8c8c8c;
  }
  * { box-sizing: border-box; margin: 0; padding: 0; }
  html, body { width: 1200px; height: 1000px; overflow: hidden; }
  body { background: var(--backdrop); position: relative; font-family: "Roboto Condensed", sans-serif; }

  .card { position: absolute; background: var(--card); box-shadow: 0 6px 18px rgba(0,0,0,.18); }

  /* Front */
  .card--front { left: 40px; top: 40px; width: 700px; height: 420px; }
  .gilded-frame {
    position: absolute; inset: 0;
    background: linear-gradient(135deg, var(--frame-dark), #b79a45 20%, #e6d28a 45%, #9c8233 70%, var(--frame-dark));
  }
  .front-panel {
    position: absolute; left: 60px; top: 62px; right: 60px; bottom: 62px;
    background: var(--card); border-radius: 10px;
    box-shadow: inset 0 0 8px rgba(0,0,0,.35);
  }
  .crest { position: absolute; left: 50%; top: 22px; width: 150px; height: 56px; transform: translateX(-50%);
    background: radial-gradient(ellipse at center, var(--ornament), rgba(201,174,98,.25) 70%, transparent); border-radius: 50%; }
  .brand-name {
    position: absolute; left: 0; right: 0; top: 88px; text-align: center;
    font-family: "Questrial", sans-serif; font-weight: 400; font-size: 42px; color: var(--gold);
    white-space: nowrap;
  }
  .brand-rule { position: absolute; left: 100px; right: 100px; top: 150px; height: 2px; background: var(--gold); }
  .contact {
    position: absolute; left: 0; right: 0; text-align: center;
    font-size: 18px; line-height: 24px; color: var(--gold-deep);
    white-space: nowrap;
  }
  .contact--top { top: 190px; }
  .contact--bottom { top: 222px; }
  .sep { display: inline-block; width: 4px; height: 20px; margin: 0 5px; vertical-align: -4px; background: var(--gold-light); }

  /* Back */
  .card--back { left: 335px; top: 490px; width: 770px; height: 475px; }
  .back-divider { position: absolute; left: 215px; top: 0; bottom: 30px; width: 3px; background: var(--gold); }
  .side-mark { position: absolute; left: 40px; top: 120px; width: 150px; height: 230px; }
  .side-crest { position: absolute; top: 60px; width: 36px; height: 110px; border-radius: 18px;
    background: linear-gradient(180deg, transparent, var(--ornament), transparent); }
  .side-crest--left { left: 5px; }
  .side-crest--right { right: 5px; }
  .side-name {
    position: absolute; left: 50%; top: 50%; width: 230px;
    transform: translate(-50%, -50%) rotate(-90deg); text-align: center;
    font-family: "Questrial", sans-serif; font-size: 22px; line-height: 24px; color: var(--silver); white-space: nowrap;
  }
  .side-rule { position: absolute; left: 93px; top: 0; width: 1px; height: 230px; background: var(--gold); }

  .booking { position: absolute; left: 250px; top: 55px; width: 460px; list-style: none; }
  .booking li {
    height: 88px; display: flex; align-items: flex-start;
    font-family: "Roboto", sans-serif; font-weight: 500; font-size: 24px; color: var(--gold-deep);
  }
  .booking li:first-child { height: 76px; }
  .booking .field { width: 100%; border-bottom: 4px solid var(--gold); padding-bottom: 2px; line-height: 26px; white-space: nowrap; }
  .clock-mark { position: absolute; left: 535px; top: 235px; width: 140px; height: 150px; border-radius: 50%;
    background: radial-gradient(circle, rgba(232,222,190,.45), rgba(232,222,190,.15) 70%, transparent); }
</style>
</head>
<body>
  <section class="card card--front" aria-label="Business card front">
    <div class="gilded-frame" role="img" aria-label="Ornate gilded picture frame border"></div>
    <div class="front-panel">
      <div class="crest" role="img" aria-label="Gold baroque scroll ornament"></div>
      <h1 class="brand-name">Velvetorchid Hair &amp; Beauty</h1>
      <div class="brand-rule"></div>
      <p class="contact contact--top">Lorinda Feltham<span class="sep"></span>Ph.: (07) 384 6139<span class="sep"></span>14 Kerewhenua Street, Taupo</p>
      <p class="contact contact--bottom">www.velvetorchid.co.nz<span class="sep"></span>hair@velvetorchid.co.nz</p>
    </div>
  </section>

  <section class="card card--back" aria-label="Business card back, appointment card">
    <div class="side-mark">
      <div class="side-crest side-crest--left" role="img" aria-label="Gold baroque scroll ornament"></div>
      <div class="side-crest side-crest--right" role="img" aria-label="Gold baroque scroll ornament"></div>
      <div class="side-rule"></div>
      <p class="side-name">Velvetorchid Hair &amp; Beauty</p>
    </div>
    <div class="back-divider"></div>
    <div class="clock-mark" role="img" aria-label="Faint alarm clock illustration"></div>
    <ul class="booking">
      <li><span class="field">Stylist:</span></li>
      <li><span class="field">Date/Time:</span></li>
      <li><span class="field">Date/Time:</span></li>
      <li><span class="field">Date/Time:</span></li>
      <li><span class="field">Date/Time:</span></li>
    </ul>
  </section>
</body>
</html>
```